Craft Brewery Beer Can Label in Alaska

Design a 16oz can label for a craft brewery.

We are making a can design that can be used for our 6 normal beers. Our desire is to have a standard design but one major element have the color change on each beer type. We included examples of how this works for others.

Elements we general like in designs - mountain scenes, waterfalls, topo map lines, hops. None/all are not required in a design but gives starting options. We are on the ocean in a glacier fjord so think mountains, glaciers and water.

Requirements
Must have
• Company Logo – provided
Forged by Frontier Logo – provided
Sovereign Maltsters Logo – provided

Alcohol warning text -

GOVERNMENT WARNING: (1) According to the Surgeon General, women should not drink alcoholic beverages during pregnancy because of the risk of birth defects. (2) Consumption of alcoholic beverages impairs your ability to drive a car or operate machinery, and may cause health problems.

Beer Name – Tide Mark Pilsner
ABV – 4.9% ABV
Size – 16 FL OZ
Nice to have
• Elements we general like in designs - mountain scenes, waterfalls, topo map lines, hops. None/all are not required in a design but gives starting options. We are on the ocean in a glacier fjord so think mountains, glaciers and water.

```html
<!DOCTYPE html>
<html lang="en">
<head>
<meta charset="utf-8">
<title>Tide Mark Pilsner – 16 oz Can Label</title>
<link rel="stylesheet" href="https://fonts.googleapis.com/css2?family=Rye&family=Abril+Fatface&family=Playfair+Display:wght@700&family=Open+Sans:wght@300;800&display=swap">
<style>
  :root {
    --stage: #e1d20a;
    --label-yellow: #f2c51f;
    --label-teal: #2bb0ad;
    --teal-deep: #17403f;
    --teal-text: #e4f4f3;
    --name-red: #e0453f;
    --label-white: #f3f3f1;
    --ice-blue: #a9d8ee;
    --brand-blue: #3a9fd0;
    --badge-grey: #4a4a4a;
  }
  * { box-sizing: border-box; margin: 0; padding: 0; }
  html, body { width: 1200px; height: 800px; overflow: hidden; background: var(--stage); }
  .canvas { position: relative; width: 1200px; height: 800px; }

  .label {
    position: absolute; left: 80px; top: 60px; width: 1040px; height: 680px;
    overflow: hidden; border-radius: 6px; background: var(--label-yellow);
    box-shadow: 0 10px 30px rgba(0,0,0,.15);
  }
  .trim { position: absolute; left: 0; width: 100%; height: 34px; background: var(--label-yellow); z-index: 3; }
  .trim::after { content: ""; position: absolute; left: 0; right: 0; height: 18px; background: var(--label-teal); }
  .trim--top { top: 0; }
  .trim--top::after { top: 10px; }
  .trim--bottom { bottom: 0; }
  .trim--bottom::after { bottom: 10px; }

  /* back panel: warning + badge */
  .back-panel {
    position: absolute; left: 0; top: 0; width: 380px; height: 100%;
    background: var(--label-teal); padding: 70px 36px 60px;
  }
  .cert-badge { width: 92px; height: 120px; background: var(--badge-grey); border-radius: 4px; margin-bottom: 28px; }
  .warning-title {
    font-family: "Playfair Display", serif; font-weight: 700; font-size: 26px;
    color: var(--teal-deep); letter-spacing: .5px; margin-bottom: 12px;
  }
  .warning-body {
    font-family: "Open Sans", sans-serif; font-weight: 300; font-size: 19px;
    line-height: 1.5; color: var(--teal-text);
  }

  /* beer name strip */
  .name-strip {
    position: absolute; left: 380px; top: 0; width: 100px; height: 100%;
    background: linear-gradient(to bottom, var(--label-yellow) 0 42%, var(--label-white) 42% 100%);
    display: flex; align-items: center; justify-content: center;
  }
  .beer-name {
    writing-mode: vertical-rl; transform: rotate(180deg);
    font-family: "Rye", serif; font-size: 46px; color: var(--name-red);
    letter-spacing: 1px; white-space: nowrap;
  }

  /* front panel */
  .front-panel { position: absolute; left: 480px; top: 0; width: 560px; height: 100%; }
  .front-panel svg { position: absolute; inset: 0; }
  .scene-art {
    position: absolute; left: 70px; top: 70px; width: 440px; height: 300px;
    border-radius: 60% 60% 8px 8px / 80% 80% 8px 8px;
    background: linear-gradient(160deg, #ffffff 0%, #cfe8f3 45%, var(--brand-blue) 100%);
  }
  .brand {
    position: absolute; left: 0; width: 100%; top: 385px; text-align: center;
    font-family: "Open Sans", sans-serif; font-weight: 800; color: var(--brand-blue);
  }
  .brand-name { font-size: 78px; line-height: 1; letter-spacing: 2px; }
  .brand-sub { font-size: 28px; letter-spacing: 22px; margin-top: 4px; padding-left: 22px; }
  .specs {
    position: absolute; left: 0; width: 100%; top: 540px; text-align: center;
    font-family: "Abril Fatface", serif; font-size: 40px; line-height: 1.2; color: var(--brand-blue);
  }
</style>
</head>
<body>
<div class="canvas">
  <div class="label">
    <div class="trim trim--top"></div>

    <section class="back-panel">
      <div class="cert-badge" aria-hidden="true"></div>
      <h2 class="warning-title">GOVERNMENT WARNING:</h2>
      <p class="warning-body">(1) According to the Surgeon General, women should not drink alcoholic beverages during pregnancy because of the risk of birth defects. (2) Consumption of alcoholic beverages impairs your ability to drive a car or operate machinery, and may cause health problems.</p>
    </section>

    <div class="name-strip">
      <h1 class="beer-name">TIDE MARK PILSNER</h1>
    </div>

    <section class="front-panel">
      <svg width="560" height="680" viewBox="0 0 560 680" aria-hidden="true">
        <rect width="560" height="680" fill="var(--label-yellow)"/>
        <path d="M0 330 C180 360 380 360 560 380 L560 680 L0 680 Z" fill="var(--label-white)"/>
        <path d="M0 610 C160 560 360 500 560 470 L560 680 L0 680 Z" fill="var(--ice-blue)"/>
      </svg>
      <div class="scene-art" role="img" aria-label="Illustration of a sea lion on a glacier peak above the fjord"></div>
      <div class="brand">
        <div class="brand-name">FJORDLINE</div>
        <div class="brand-sub">BREWING</div>
      </div>
      <div class="specs">
        <p>ABV – 4.9% ABV</p>
        <p>16 FL OZ</p>
      </div>
    </section>

    <div class="trim trim--bottom"></div>
  </div>
</div>
</body>
</html>
```